Sticker for the front of our product

Design a sticker for the front of our stain removal kit.

We have provided some images and rough drafts of what we want the sticker to look like. Basically, our product is called the Carpet stain removal "Swift Pack"and our company is called "Brindle Vane. Also, our slogan is, "it's what the professionals use".

We really would like the product name ( Carpet stain removal "Swift Pack ), slogan ( it's what the professionals use ), and company logo (Brindle Vane) to be on the front sticker, as well as a spilling glass of red wine. We have also provided a word doc draft with red wine & a dog wee stain picture, we would also like to see how these two can be used together (we cannot attached the dog file as its to big, we can email it across).

The spilling glass of wine would be our preference, however, feel free to experiment with other ideas including the dog wee picture.

The dimensions of the sticker need to be as follows, 200mm x 65mm (20cm width, 6.5cm height)

I have provided our logo bellow ( Brindle Vane ) please incorporate this somewhere in the corner of the sticker.

Please make the words "stain removal" the most noticeable words in the sticker as we want people to be drawn to the function of the product. Please add the words "Swift Pack" too, however, not as prominent. Use our drafts as a rough guide for your design.

Our product is quality and expensive and we want our front sticker to look as professional and quality as the product inside it.
Our intended market for customers to purchase this product are 18-65 years.

We have purchased some photos from Picvora of the red wine, dog wee, coffee sill, paint and coke. These are also too large to upload. We can email these across is necessary.

```html
<!DOCTYPE html>
<html lang="en">
<head>
<meta charset="utf-8">
<title>Brindle Vane – Carpet Stain Removal Sticker</title>
<link rel="stylesheet" href="https://fonts.googleapis.com/css2?family=Montserrat:wght@300;400;500;700&family=PT+Serif:ital@1&family=Arimo&display=swap">
<style>
  :root {
    --backdrop: #a9aaad;
    --sticker: #ffffff;
    --brand-blue: #1b96cd;
    --title-red: #e3323f;
    --ink-dark: #3b3b3b;
    --ink-grey: #777777;
    --rule: #444444;
    --wine-deep: #c7283d;
    --wine-light: #f1a4ae;
    --glass: #e9ecef;
  }
  * { box-sizing: border-box; margin: 0; padding: 0; }
  html, body { width: 1200px; height: 969px; overflow: hidden; }
  body {
    background: var(--backdrop);
    position: relative;
    border: 1px solid #555;
  }
  .sticker {
    position: absolute;
    left: 151px; top: 273px;
    width: 975px; height: 421px;
    background: var(--sticker);
  }
  .front {
    position: absolute;
    left: 0; top: 0;
    width: 470px; height: 373px;
  }
  .brand {
    position: absolute;
    left: 0; width: 470px; top: 30px;
    display: flex; align-items: center; justify-content: center; gap: 6px;
    font-family: "Montserrat", sans-serif;
    font-weight: 700;
    font-size: 16px;
    letter-spacing: 0.5px;
    color: var(--brand-blue);
  }
  .brand-mark {
    width: 10px; height: 10px;
    background: var(--brand-blue);
  }
  .product-title {
    position: absolute;
    left: 0; width: 470px; top: 84px;
    text-align: center;
    font-family: "Montserrat", sans-serif;
    color: var(--title-red);
    line-height: 1;
  }
  .product-title .category {
    display: block;
    font-weight: 400;
    font-size: 29px;
    letter-spacing: 3px;
  }
  .product-title .function {
    display: block;
    margin-top: 5px;
    font-weight: 700;
    font-size: 27px;
    letter-spacing: 2.4px;
  }
  .slogan {
    position: absolute;
    left: 0; width: 470px; top: 141px;
    text-align: center;
    font-family: "PT Serif", serif;
    font-style: italic;
    font-size: 15px;
    color: var(--ink-dark);
  }
  .wine-visual {
    position: absolute;
    left: 67px; top: 130px;
    width: 366px; height: 228px;
    border-radius: 4px;
    background:
      radial-gradient(ellipse at 30% 60%, var(--wine-deep) 0%, var(--wine-light) 38%, rgba(255,255,255,0) 62%),
      radial-gradient(ellipse at 75% 45%, var(--glass) 0%, rgba(255,255,255,0) 45%),
      linear-gradient(180deg, #ffffff 0%, #f5f5f5 100%);
    z-index: 0;
  }
  .product-title, .slogan, .brand { z-index: 1; }
  .divider {
    position: absolute;
    left: 470px; top: 11px;
    width: 1px; height: 355px;
    background: var(--rule);
  }
  .instructions {
    position: absolute;
    left: 495px; top: 36px;
    font-family: "Arimo", sans-serif;
    font-size: 16px;
    color: var(--ink-grey);
  }
  .kit-band {
    position: absolute;
    left: 0; bottom: 0;
    width: 975px; height: 48px;
    background: var(--brand-blue);
  }
  .kit-name {
    position: absolute;
    left: 173px; top: 8px;
    font-family: "Montserrat", sans-serif;
    font-weight: 500;
    font-size: 28px;
    font-variant: small-caps;
    letter-spacing: 0.5px;
    color: #ffffff;
    line-height: 1;
  }
</style>
</head>
<body>
  <section class="sticker">
    <div class="front">
      <div class="brand"><span class="brand-mark"></span>Brindle Vane</div>
      <div class="wine-visual" role="img" aria-label="Photograph of a tipping wine glass spilling a splash of red wine"></div>
      <h1 class="product-title">
        <span class="category">CARPET</span>
        <span class="function">STAIN REMOVAL</span>
      </h1>
      <p class="slogan">It's what the professionals use</p>
    </div>
    <div class="divider"></div>
    <p class="instructions">How to use:</p>
    <div class="kit-band">
      <span class="kit-name">Swift Pack</span>
    </div>
  </section>
</body>
</html>
```